BUSINESS CARD - HALLORAN FIELD SERVICES

I would like to create a business card for my fertilizer spreading business. I would like to incorporate my existing logo and also a description of the services offered. The business card will be given to farmers so must be kept simple but effective. It will also be left in stores so much also be eye catching in order to stand out from other cards.

Target Market(s)

FARMERS

Requirements
Must have
• FRONT OF CARD = EXISTING LOGO + "CUSTOMISED SPREADING" below the logo

REAR Of CARD = SERVICES OFFERED AND CONTACT DETAILS

- Bulk fertilizer including Lime, Gypsum, Manure & Compost
- Granular fertilizer including Single Super, Urea, Gran-am, & Custom Blends
- Modern equipment - Autosteer & Variable Rate Capable
- Friendly & Reliable Service
- Contact Gus: 0471 592 318
Nice to have
• utilize same color scheme as existing logo

```html
<!DOCTYPE html>
<html lang="en">
<head>
<meta charset="utf-8">
<title>Halloran Field Services — Business Card</title>
<link href="https://fonts.googleapis.com/css2?family=Open+Sans:wght@400;600;700&family=Saira:wght@700&display=swap" rel="stylesheet">
<style>
  :root {
    --backdrop: #2a2a2c;
    --card-white: #ffffff;
    --card-dark: #1c1c1e;
    --ink-grey: #555557;
    --mark-grey: #5a5a5c;
    --rule-grey: #a6a6a6;
    --accent-orange: #f39116;
    --pattern-tone: #242426;
  }
  * { box-sizing: border-box; margin: 0; padding: 0; }
  html, body { width: 1200px; height: 1108px; overflow: hidden; }
  body {
    background: var(--backdrop);
    font-family: "Open Sans", sans-serif;
    display: flex;
    align-items: center;
    justify-content: center;
    gap: 60px;
  }
  .card {
    width: 400px;
    height: 680px;
    border-radius: 22px;
    position: relative;
    overflow: hidden;
  }
  /* Rear: services */
  .card--rear {
    background: var(--card-white);
    color: var(--ink-grey);
    text-align: center;
    padding: 56px 20px 0;
  }
  .brand-mark {
    width: 130px; height: 130px;
    margin: 0 auto;
    border-radius: 50%;
    background: var(--mark-grey);
  }
  .brand-name {
    margin-top: 20px;
    font-weight: 700;
    font-size: 24px;
    letter-spacing: 0.5px;
    line-height: 1.15;
    color: var(--ink-grey);
  }
  .services {
    list-style: none;
    margin-top: 34px;
    font-size: 14px;
    line-height: 1.6;
    text-transform: uppercase;
    letter-spacing: 0.2px;
  }
  .services li { white-space: nowrap; }
  .contact {
    margin: 36px 24px 0;
  }
  .contact__label {
    display: flex;
    align-items: center;
    gap: 10px;
    font-weight: 700;
    font-size: 21px;
    color: var(--ink-grey);
  }
  .contact__label::before,
  .contact__label::after {
    content: "";
    flex: 1;
    height: 1px;
    background: var(--rule-grey);
  }
  .contact__line {
    margin-top: 4px;
    font-weight: 700;
    font-size: 21px;
    white-space: nowrap;
  }
  .contact__phone {
    color: var(--accent-orange);
    font-size: 27px;
    font-weight: 600;
  }
  /* Front: logo + tagline */
  .card--front {
    background: var(--card-dark);
    display: flex;
    flex-direction: column;
    align-items: center;
  }
  .pattern-field {
    position: absolute;
    inset: 0 0 220px 0;
    background: linear-gradient(180deg, var(--pattern-tone), var(--card-dark));
  }
  .front-lockup {
    position: relative;
    margin-top: 390px;
    text-align: center;
  }
  .front-lockup .brand-mark {
    width: 100px; height: 100px;
  }
  .front-lockup .brand-name {
    margin-top: 12px;
    font-size: 14px;
    color: var(--mark-grey);
  }
  .tagline {
    position: relative;
    margin-top: 48px;
    font-family: "Saira", sans-serif;
    font-weight: 700;
    font-size: 27px;
    letter-spacing: 2px;
    color: var(--accent-orange);
    white-space: nowrap;
  }
</style>
</head>
<body>
  <section class="card card--rear" aria-label="Card rear: services and contact">
    <div class="brand-mark"></div>
    <h1 class="brand-name">HALLORAN FIELD<br>SERVICES</h1>
    <ul class="services">
      <li>Bulk fertilizer including lime</li>
      <li>Gypsum, manure &amp; compost</li>
      <li>Granular fertilizer including single</li>
      <li>Super, urea, gran-am, &amp; custom blends</li>
      <li>Modern equipment</li>
      <li>Autosteer &amp; variable rate capable</li>
      <li>Friendly &amp; reliable service</li>
    </ul>
    <div class="contact">
      <p class="contact__label">CONTACT</p>
      <p class="contact__line">GUS: <span class="contact__phone">0471 592 318</span></p>
    </div>
  </section>

  <section class="card card--front" aria-label="Card front: brand and tagline">
    <div class="pattern-field" role="img" aria-label="Faint repeated brand symbol pattern"></div>
    <div class="front-lockup">
      <div class="brand-mark"></div>
      <p class="brand-name">HALLORAN FIELD SERVICES</p>
    </div>
    <p class="tagline">CUSTOMISED SPREADING</p>
  </section>
</body>
</html>
```